The Lantern Protocol: A Practical Guide for Tending Old Orchards

This will be for both the hard cover and paperback version. A core theme of the book and what we want to cover to convey is the journey or transformation to "happiness". Concepts such as road/pathway, mountain top, sunrise, dark to bright colors, out-of-focus to in-focus, clouds parting, etc., all represent this idea. I am attaching a 1-page book summary for more information. I like the idea of the subtitle being in a gold seal, but that is not necessary. I am open to any designs, but it should at least be conceptually related to the book.

```html
<!DOCTYPE html>
<html lang="en">
<head>
<meta charset="utf-8">
<title>The Lantern Protocol — Cover</title>
<link rel="stylesheet" href="https://fonts.googleapis.com/css2?family=Almendra:wght@400;700&family=Federo&family=Alike&display=swap">
<style>
  :root {
    --page-bg: #ffffff;
    --title-white: #ffffff;
    --title-pink: #d93f83;
    --text-shadow: rgba(40, 25, 20, 0.55);
    --sky-top: #6d8791;
    --sky-mid: #b9c9c9;
    --glow: #e9a577;
    --sun: #f6d2a8;
    --earth-mid: #8a4a33;
    --earth-dark: #2c1714;
  }
  * { margin: 0; padding: 0; box-sizing: border-box; }
  html, body {
    width: 1200px;
    height: 960px;
    overflow: hidden;
    background: var(--page-bg);
  }
  .canvas {
    position: relative;
    width: 1200px;
    height: 960px;
  }
  .cover {
    position: absolute;
    left: 300px;
    top: 30px;
    width: 600px;
    height: 900px;
    overflow: hidden;
  }
  .cover-photo {
    position: absolute;
    inset: 0;
    width: 100%;
    height: 100%;
  }
  .cover-title {
    position: absolute;
    left: 0;
    right: 0;
    top: 22px;
    text-align: center;
    line-height: 1;
  }
  .title-lead {
    display: block;
    font-family: "Almendra", serif;
    font-weight: 400;
    font-size: 76px;
    color: var(--title-white);
    letter-spacing: 1px;
    text-shadow: 2px 3px 3px var(--text-shadow);
  }
  .title-main {
    display: block;
    margin-top: 6px;
    font-family: "Almendra", serif;
    font-weight: 400;
    font-size: 84px;
    color: var(--title-pink);
    letter-spacing: 1px;
    text-shadow: 2px 3px 3px var(--text-shadow);
  }
  .cover-subtitle {
    position: absolute;
    left: 0;
    right: 0;
    top: 650px;
    text-align: center;
    font-family: "Federo", sans-serif;
    font-size: 36px;
    line-height: 1.45;
    color: var(--title-white);
    text-shadow: 1px 2px 3px var(--text-shadow);
  }
  .cover-author {
    position: absolute;
    right: 54px;
    top: 818px;
    font-family: "Alike", serif;
    font-weight: 700;
    font-size: 31px;
    color: var(--title-white);
    letter-spacing: 0.5px;
    text-shadow: 1px 2px 3px var(--text-shadow);
  }
</style>
</head>
<body>
<div class="canvas">
  <section class="cover">
    <svg class="cover-photo" viewBox="0 0 600 900" preserveAspectRatio="none" role="img"
         aria-label="Photograph of a winding mountain road at sunrise, with parting clouds, a glowing sun behind a tree-covered hillside and dark asphalt in the foreground">
      <defs>
        <linearGradient id="scene" x1="0" y1="0" x2="0" y2="1">
          <stop offset="0" stop-color="var(--sky-top)"/>
          <stop offset="0.25" stop-color="var(--sky-mid)"/>
          <stop offset="0.5" stop-color="var(--glow)"/>
          <stop offset="0.68" stop-color="var(--earth-mid)"/>
          <stop offset="1" stop-color="var(--earth-dark)"/>
        </linearGradient>
        <radialGradient id="sunGlow" cx="0.52" cy="0.57" r="0.4">
          <stop offset="0" stop-color="var(--sun)" stop-opacity="0.9"/>
          <stop offset="1" stop-color="var(--sun)" stop-opacity="0"/>
        </radialGradient>
      </defs>
      <rect width="600" height="900" fill="url(#scene)"/>
      <rect width="600" height="900" fill="url(#sunGlow)"/>
    </svg>

    <h1 class="cover-title">
      <span class="title-lead">The Lantern</span>
      <span class="title-main">PROTOCOL</span>
    </h1>

    <p class="cover-subtitle">A Practical Guide for Tending<br>Old Orchards</p>

    <p class="cover-author">EDWIN R. HALLOWAY</p>
  </section>
</div>
</body>
</html>
```